ZEPRILO.COM is a premium domain sales company. Our competitors are companies like vastplots.example, getparcels.example, peerwords.example. Our current site is at www.zeprilos.example.

We want to have the ability to search for domains, to highlight special offers and have some testimonials on the index page.

The logo for the site is attached.

Please be sure that the order form fits on the screen without scrolling the page. I want the entire form, including the submit button to fit without any page scrolling.

Delivered product - INDEX PAGE, ORDER FORM AND CONTENT PAGE PSDs.

Target Market(s)

Small to Medium business professionals

Industry/Entity Type

It Company

Requirements
Must have
• 1. List of domains for sale
2. Simple search box with button to run the search
3. link for advanced search
4. testimonial area. Note - this can be a small box where a different testimonial is displayed on each page load.
Nice to have
• Would like the site to have some white space. Don't want a heavily packed website. Give it an "airy" feel.

```html
<!DOCTYPE html>
<html lang="en">
<head>
<meta charset="utf-8">
<title>ZEPRILO.COM — Premium Domains</title>
<link href="https://fonts.googleapis.com/css2?family=Figtree:wght@400;500;600;700&family=PT+Serif:ital@1&display=swap" rel="stylesheet">
<style>
:root{
  --nav-green:#1c7444;
  --active-green:#5c9c2e;
  --hero-blue:#16519a;
  --brand-blue:#1e4f9a;
  --panel-blue:#1a5aa6;
  --link-green:#3fe06a;
  --hero-sub:#9cc3f0;
  --text:#222;
  --muted:#666;
  --row:#f1f1f1;
  --line:#e2e6ee;
  --footer:#f2f2f2;
  --star:#f39a1e;
}
*{box-sizing:border-box;margin:0;padding:0}
html,body{width:1200px;height:1000px;overflow:hidden;background:#fff;font-family:"Figtree",Arial,sans-serif;color:var(--text)}
.page{position:relative;width:1200px;height:1000px}
.abs{position:absolute}

.brand{left:258px;top:14px;font-size:30px;font-weight:700;color:var(--brand-blue);letter-spacing:-.5px}
.call{left:811px;top:22px;font-size:10px;color:#333}
.call strong{display:block;font-size:17px;font-weight:700;color:var(--brand-blue);margin-top:1px}

.nav{left:101px;top:60px;width:998px;height:35px;background:var(--nav-green)}
.nav ul{list-style:none;display:flex;position:absolute;left:157px;top:7px}
.nav li{font-size:12px;font-weight:500;color:#fff;letter-spacing:.5px;padding:4px 11px;margin-right:6px;border-radius:2px}
.nav li.active{background:var(--active-green)}

.hero{left:101px;top:95px;width:998px;height:281px;background:var(--hero-blue)}
.hero h1{position:absolute;left:170px;top:45px;font-size:23px;font-weight:600;line-height:26px;color:#fff;width:360px}
.hero p.lead{position:absolute;left:171px;top:132px;font-size:16px;line-height:21px;color:var(--hero-sub);width:360px}
.search{position:absolute;left:176px;top:195px;width:368px;height:42px;background:#ececec;border-radius:3px;box-shadow:0 1px 3px rgba(0,0,0,.3)}
.search .tld{position:absolute;left:193px;top:8px;font-size:20px;color:#777;font-weight:500;border-left:2px solid #bbb;padding-left:8px}
.search .tld span{font-size:11px;vertical-align:3px;margin-right:4px}
.search .btn{position:absolute;left:277px;top:8px;width:84px;height:26px;background:var(--nav-green);color:#fff;font-size:12px;font-weight:700;letter-spacing:.8px;text-align:center;line-height:26px}
.hint{position:absolute;left:183px;top:242px;font-size:11px;color:#e6eefa}
.hint a{color:var(--link-green);font-size:12px;margin-left:6px;text-decoration:underline}
.photo{position:absolute;left:572px;top:8px;width:270px;height:273px;border-radius:120px 120px 0 0;background:linear-gradient(180deg,#2e62a8 0%,#b23a3e 55%,#d23036 100%)}
.caption{position:absolute;left:752px;top:238px;font-size:9px;font-weight:700;color:#fff;line-height:11px}
.caption small{display:block;font-size:7px;font-weight:500}

.quote{left:270px;top:395px;width:410px}
.quote p{font-family:"PT Serif",Georgia,serif;font-style:italic;font-size:13.5px;line-height:17.5px;color:#777;padding-left:21px}
.quote .qmark{position:absolute;font-family:Georgia,serif;font-size:28px;font-weight:700;line-height:1}
.quote .open{left:0;top:0;color:var(--brand-blue)}
.quote .close{left:402px;top:41px;color:var(--nav-green)}

.domains{left:258px;top:471px;width:431px;height:315px;border:1px solid var(--line);border-radius:3px}
.domains table{position:absolute;left:10px;top:8px;width:408px;border-collapse:collapse}
.domains th{text-align:left;font-size:13.5px;font-weight:700;height:31px;border-bottom:2px solid var(--line);letter-spacing:.3px}
.domains th,.domains td{padding-left:13px}
.domains td{font-size:14px;height:34.2px}
.domains tr.alt td{background:var(--row)}
.domains thead tr th:first-child{width:194px}
.domains thead tr th:nth-child(2){width:98px}
.spacer td{height:9px!important;padding:0}

.card{left:706px;width:236px;border-radius:3px;overflow:hidden}
.card h3{height:32px;background:var(--panel-blue);color:#fff;font-size:13.5px;font-weight:600;line-height:32px;padding-left:14px}
.newsletter{top:395px;background:#ededed;height:141px}
.newsletter p{font-size:10.5px;line-height:17px;color:#444;padding:13px 14px 0}
.newsletter .email{position:absolute;left:14px;top:100px;width:135px;height:27px;background:#fff;border:1px solid #d4d4d4;border-radius:3px;font-size:9px;font-weight:600;padding:8px 10px}
.newsletter .sub{position:absolute;left:156px;top:100px;width:71px;height:27px;background:var(--panel-blue);color:#fff;font-size:11.5px;text-align:center;line-height:25px;border-radius:3px;border:1px solid #154d91}
.feature{top:572px;height:175px;border:1px solid var(--line)}
.feature h3{margin:-1px -1px 0;letter-spacing:.5px}
.feature ul{list-style:none;padding:8px 0 0 10px}
.feature li{display:flex;align-items:center;font-size:12.5px;height:25.7px}
.feature li svg{margin-right:11px}
.feature li .name{width:135px}

.footer{left:101px;top:801px;width:998px;height:199px;background:var(--footer)}
.fcol{position:absolute;top:22px}
.fcol h4{font-size:15px;font-weight:600;color:#555;font-variant:small-caps;letter-spacing:1.2px;margin-bottom:12px}
.fcol li{list-style:none;font-size:11px;line-height:17px;color:#555;font-weight:500}
.fcol .email{width:135px;height:27px;background:#fff;border:1px solid #ddd;border-radius:3px;font-size:9px;font-weight:600;padding:8px 10px;margin-top:0}
.fcol .sub{width:71px;height:27px;background:var(--panel-blue);color:#fff;font-size:11.5px;text-align:center;line-height:25px;border-radius:3px;margin-top:7px}
.fbrand{font-size:24px;font-weight:700;color:var(--brand-blue);margin-bottom:12px}
.fcol address{font-style:normal;font-size:11px;line-height:17px;color:#555;font-weight:500}
.legal{position:absolute;top:183px;font-size:8.5px;color:#444}
.legal.right{left:605px}
.legal.right span{margin:0 6px;color:#999}
</style>
</head>
<body>
<div class="page">

  <div class="abs brand">ZEPRILO.COM</div>
  <div class="abs call">Call Us Now!<strong>0 800 5550 1942</strong></div>

  <nav class="abs nav">
    <ul>
      <li class="active">HOME</li>
      <li>CONTACT US</li>
      <li>DOMAINS SALE</li>
      <li>TESTIMONIALS</li>
      <li>CART</li>
    </ul>
  </nav>

  <section class="abs hero">
    <h1>Impression of Your business could be started from Name of the Domain itself.</h1>
    <p class="lead">Let’ your Door is wide open to the world by buying this below PREMIUM DOMAIN!</p>
    <div class="search">
      <div class="tld"><span>▼</span>.com</div>
      <div class="btn">SEARCH</div>
    </div>
    <p class="hint">Find your domain name on the box above. <a>Advance search</a></p>
    <div class="photo" role="img" aria-label="Photo of a happy domain owner in a red top cheering with raised fists"></div>
    <div class="caption">Marla Quint<small>Domain Owner</small></div>
  </section>

  <blockquote class="abs quote">
    <span class="qmark open">“</span>
    <p>Nullam quis risus eget urna mollis ornare vel eu leo. Donec sed odio dui. Curabitur blandit tempus porttitor. Vestibulum id ligula porta felis euismod semper.</p>
    <span class="qmark close">”</span>
  </blockquote>

  <div class="abs domains">
    <table>
      <thead><tr><th>DOMAIN</th><th>PRIZE</th><th>BUY</th></tr></thead>
      <tbody>
        <tr class="spacer"><td colspan="3"></td></tr>
        <tr class="alt"><td>DomainName1.com</td><td>$1,005</td><td>Buy Now!</td></tr>
        <tr><td>DomainName2.com</td><td>$1,005</td><td>Buy Now!</td></tr>
        <tr class="alt"><td>DomainName3.com</td><td>$1,005</td><td>Buy Now!</td></tr>
        <tr><td>DomainName4.com</td><td>$1,005</td><td>Buy Now!</td></tr>
        <tr class="alt"><td>DomainName5.com</td><td>$1,005</td><td>Buy Now!</td></tr>
        <tr><td>DomainName6.com</td><td>$1,005</td><td>Buy Now!</td></tr>
        <tr class="alt"><td>DomainName17com</td><td>$1,005</td><td>Buy Now!</td></tr>
      </tbody>
    </table>
  </div>

  <aside class="abs card newsletter">
    <h3>Join Our Newsletter</h3>
    <p>Get Awesome OFFER from us with join in our FREE Newsletter today.</p>
    <div class="email">E-mail here</div>
    <div class="sub">Subscribe</div>
  </aside>

  <aside class="abs card feature">
    <h3>FEATURE DOMAINS</h3>
    <ul>
      <li><svg width="9" height="9" viewBox="0 0 10 10"><path d="M5 0l1.5 3.3 3.5.4-2.6 2.3.8 3.5L5 7.7 1.8 9.5l.8-3.5L0 3.7l3.5-.4z" fill="var(--star)"/></svg><span class="name">DomainName #1</span>$14,500</li>
      <li><svg width="9" height="9" viewBox="0 0 10 10"><path d="M5 0l1.5 3.3 3.5.4-2.6 2.3.8 3.5L5 7.7 1.8 9.5l.8-3.5L0 3.7l3.5-.4z" fill="var(--star)"/></svg><span class="name">DomainName #2</span>$12,500</li>
      <li><svg width="9" height="9" viewBox="0 0 10 10"><path d="M5 0l1.5 3.3 3.5.4-2.6 2.3.8 3.5L5 7.7 1.8 9.5l.8-3.5L0 3.7l3.5-.4z" fill="var(--star)"/></svg><span class="name">DomainName #3</span>$11,500</li>
      <li><svg width="9" height="9" viewBox="0 0 10 10"><path d="M5 0l1.5 3.3 3.5.4-2.6 2.3.8 3.5L5 7.7 1.8 9.5l.8-3.5L0 3.7l3.5-.4z" fill="var(--star)"/></svg><span class="name">DomainName #4</span>$9,500</li>
      <li><svg width="9" height="9" viewBox="0 0 10 10"><path d="M5 0l1.5 3.3 3.5.4-2.6 2.3.8 3.5L5 7.7 1.8 9.5l.8-3.5L0 3.7l3.5-.4z" fill="var(--star)"/></svg><span class="name">DomainName #5</span>$8,500</li>
    </ul>
  </aside>

  <footer class="abs footer">
    <div class="fcol" style="left:171px">
      <h4>Main Menu</h4>
      <ul><li>Home</li><li>Contact Us</li><li>Domains Sale</li><li>Testimonials</li><li>Cart</li></ul>
    </div>
    <div class="fcol" style="left:304px">
      <h4>How It Works</h4>
      <ul><li>Aenean lacinia bibendum</li><li>Pellentesque ornare sem</li><li>Vestibulum id ligula porta</li><li>Nullam quis risus eget urna</li><li>Praesent commodo cursus</li></ul>
    </div>
    <div class="fcol" style="left:484px">
      <h4>Advance Search</h4>
      <div class="email">E-mail here</div>
      <div class="sub">Subscribe</div>
    </div>
    <div class="fcol" style="left:669px;top:18px">
      <div class="fbrand">ZEPRILO.COM</div>
      <address>(c) 2013 Zeprilo, Inc.<br>1480 Harrow Lane<br>Suite 210<br>Brookfield, TN 37999<br>United States</address>
    </div>
    <p class="legal" style="left:171px">(C) Copyright 2013. Zeprilo Inc. All rights reserved.</p>
    <p class="legal right">Universal Terms<span>|</span>Refund Policy<span>|</span>Privacy Policy</p>
  </footer>

</div>
</body>
</html>
```